R&t subterra

We specialize in CIPP pipe lining but do other underground utilities trenchless as well.

Target Market(s)

Trenchless sewer replacement

Contact Information for Business Card

Doug Falvey 715-482-6170 Pine hollow, wi

```html
<!DOCTYPE html>
<html lang="en">
<head>
<meta charset="utf-8">
<title>R&amp;t subterra — Business Card</title>
<link href="https://fonts.googleapis.com/css2?family=Montserrat:wght@400;500;700;800&display=swap" rel="stylesheet">
<style>
  :root {
    --stage: #2b2b2d;
    --brand-blue: #2a86c8;
    --sky-blue: #8fc3e8;
    --card-white: #ffffff;
    --card-grey: #e4e4e6;
    --ink: #3c3c3e;
    --rule: #d6d6d8;
  }
  * { margin: 0; padding: 0; box-sizing: border-box; }
  html, body {
    width: 1200px;
    height: 900px;
    overflow: hidden;
    background: var(--stage);
    font-family: "Montserrat", sans-serif;
  }
  .canvas {
    position: relative;
    width: 1200px;
    height: 900px;
  }
  .card {
    position: absolute;
    width: 560px;
    height: 320px;
    border-radius: 26px;
    overflow: hidden;
  }
  .card--front {
    left: 150px;
    top: 70px;
    background: radial-gradient(ellipse at 50% 50%, var(--card-white) 0%, #eef3f8 40%, var(--sky-blue) 100%);
    display: flex;
    align-items: center;
    justify-content: center;
  }
  .card--back {
    left: 490px;
    top: 500px;
    background: linear-gradient(120deg, var(--card-grey) 0%, var(--card-white) 60%, #f4f4f5 100%);
  }
  .brand {
    display: flex;
    align-items: center;
    gap: 14px;
    color: var(--brand-blue);
    font-weight: 800;
    text-transform: uppercase;
    letter-spacing: 1px;
  }
  .brand__dot {
    border-radius: 50%;
    background: var(--brand-blue);
    flex: none;
  }
  .card--front .brand { font-size: 40px; }
  .card--front .brand__dot { width: 34px; height: 34px; }

  .card--back .brand {
    position: absolute;
    left: 120px;
    top: 66px;
    font-size: 36px;
  }
  .card--back .brand__dot { width: 30px; height: 30px; }

  .holder {
    position: absolute;
    left: 0;
    right: 0;
    top: 168px;
    text-align: center;
  }
  .holder__name {
    color: var(--brand-blue);
    font-size: 21px;
    font-weight: 500;
    text-transform: uppercase;
    letter-spacing: 0.5px;
  }
  .holder__rule {
    width: 400px;
    height: 1px;
    margin: 18px auto 16px;
    background: var(--rule);
  }
  .contact {
    display: flex;
    justify-content: center;
    align-items: center;
    gap: 8px;
    color: var(--ink);
    font-size: 17px;
    font-weight: 400;
  }
  .contact svg { width: 16px; height: 16px; fill: var(--brand-blue); flex: none; }
  .contact__sep { color: var(--ink); margin: 0 2px; }
</style>
</head>
<body>
<main class="canvas">
  <section class="card card--front" aria-label="Card front">
    <div class="brand"><span class="brand__dot"></span><span>R&amp;t subterra</span></div>
  </section>

  <section class="card card--back" aria-label="Card back">
    <div class="brand"><span class="brand__dot"></span><span>R&amp;t subterra</span></div>
    <div class="holder">
      <p class="holder__name">Doug Falvey</p>
      <div class="holder__rule"></div>
      <p class="contact">
        <svg viewBox="0 0 24 24" aria-hidden="true"><path d="M6.6 10.8a15.1 15.1 0 0 0 6.6 6.6l2.2-2.2c.3-.3.7-.4 1-.2 1.1.4 2.3.6 3.6.6.6 0 1 .4 1 1V20c0 .6-.4 1-1 1A17 17 0 0 1 3 4c0-.6.4-1 1-1h3.5c.6 0 1 .4 1 1 0 1.3.2 2.5.6 3.6.1.3 0 .7-.2 1z"/></svg>
        <span>715-482-6170</span>
        <span class="contact__sep">|</span>
        <svg viewBox="0 0 24 24" aria-hidden="true"><path d="M12 2a7 7 0 0 0-7 7c0 5.2 7 13 7 13s7-7.8 7-13a7 7 0 0 0-7-7zm0 9.5A2.5 2.5 0 1 1 12 6.5a2.5 2.5 0 0 1 0 5z"/></svg>
        <span>Pine hollow, wi</span>
      </p>
    </div>
  </section>
</main>
</body>
</html>
```